Bright Path Therapies business cards and stationary

Need business cards and stationary designed to match previously made logo for for a new company based in Sydney NSW called 'Bright Path Therapies'.

We provide early intervention services and diagnostic assessment for children with disability and their families. I would like designs that are colourful and child friendly - possibly using feet/footprints/steps on a white background. The final design should communicate that we are family friendly, accepting and fun to work with.

Target Market(s)

Parents and Families
Teachers
Allied Health Professionals

Industry/Entity Type

Psychology

Contact Information for Business Card

Bright Path Therapies
www.brightpaththerapies.example
info@brightpaththerapies.example

Font styles to use
Sans Serif
Decorative
Script

Requirements
Must have
• Match the font and colour scheme of logo, along with footprint picture
Nice to have
• Clean and simple, while reflecting that I am working with families.
• Also- editable for when we make staff specific cards.

```html
<!DOCTYPE html>
<html lang="en">
<head>
<meta charset="utf-8">
<title>Bright Path Therapies – Business Card</title>
<link href="https://fonts.googleapis.com/css2?family=Open+Sans:wght@400;600;700&display=swap" rel="stylesheet">
<style>
  :root {
    --backdrop: #2b2b2d;
    --brand-blue: #2a72c0;
    --brand-blue-light: #3b82cc;
    --brand-red: #e2352f;
    --ink: #1e1e1e;
    --paper: #ffffff;
    --faint: #f0f0f0;
  }
  * { box-sizing: border-box; margin: 0; padding: 0; }
  html, body { width: 1200px; height: 900px; overflow: hidden; }
  body {
    background: var(--backdrop);
    font-family: "Open Sans", Arial, sans-serif;
    position: relative;
  }
  .card {
    position: absolute;
    left: 250px;
    width: 700px;
    height: 400px;
    overflow: hidden;
    box-shadow: 0 10px 24px rgba(0,0,0,0.45);
  }
  /* ---------- front ---------- */
  .card-front {
    top: 35px;
    background: var(--brand-blue);
  }
  .card-front .faint-decor {
    position: absolute;
    left: 30px; top: 20px;
    width: 150px; height: 360px;
    border-radius: 50%;
    background: radial-gradient(ellipse at center, rgba(255,255,255,0.07), rgba(255,255,255,0) 70%);
  }
  .brand {
    display: flex;
    align-items: center;
    gap: 18px;
  }
  .brand-dot {
    width: 84px; height: 84px;
    border-radius: 50%;
    background: var(--brand-red);
    flex: none;
  }
  .brand-name {
    font-weight: 600;
    line-height: 1.05;
    letter-spacing: 0.02em;
  }
  .card-front .brand {
    position: absolute;
    left: 190px; top: 120px;
  }
  .card-front .brand-name {
    color: var(--paper);
    font-size: 40px;
  }
  .card-front .web {
    position: absolute;
    left: 0; right: 0; top: 318px;
    text-align: center;
    color: var(--paper);
    font-size: 18px;
    letter-spacing: 0.08em;
  }
  /* ---------- back ---------- */
  .card-back {
    top: 470px;
    background: var(--paper);
  }
  .card-back .faint-decor {
    position: absolute;
    right: 30px; top: 120px;
    width: 180px; height: 260px;
    border-radius: 50%;
    background: radial-gradient(ellipse at center, var(--faint), rgba(240,240,240,0) 70%);
  }
  .card-back .brand {
    position: absolute;
    left: 45px; top: 40px;
  }
  .card-back .brand-name {
    color: var(--brand-blue);
    font-size: 36px;
  }
  .contact {
    position: absolute;
    left: 60px; top: 165px;
    font-size: 19px;
    color: var(--ink);
    line-height: 1.45;
    list-style: none;
  }
  .contact li { display: flex; align-items: center; gap: 8px; }
  .contact .icon { width: 18px; height: 18px; flex: none; }
  .contact .address { padding-left: 26px; }
  .staff {
    position: absolute;
    left: 440px; top: 240px;
  }
  .staff-name {
    color: var(--brand-red);
    font-weight: 700;
    font-size: 26px;
  }
  .staff-role {
    color: var(--ink);
    font-size: 19px;
  }
  .band {
    position: absolute;
    left: 0; bottom: 0;
    width: 700px; height: 110px;
  }
  .card-back .web {
    position: absolute;
    right: 24px; bottom: 16px;
    color: var(--paper);
    font-size: 20px;
    letter-spacing: 0.02em;
  }
</style>
</head>
<body>

<section class="card card-front">
  <div class="faint-decor" role="img" aria-label="Faint decorative area in light blue"></div>
  <div class="brand">
    <span class="brand-dot"></span>
    <span class="brand-name">Bright Path<br>Therapies</span>
  </div>
  <p class="web">www.brightpaththerapies.example</p>
</section>

<section class="card card-back">
  <div class="faint-decor" role="img" aria-label="Faint decorative area in light grey"></div>
  <div class="brand">
    <span class="brand-dot"></span>
    <span class="brand-name">Bright Path<br>Therapies</span>
  </div>

  <ul class="contact">
    <li class="address">48 Harbour Lane</li>
    <li class="address">Glenmore NSW 2000</li>
    <li>
      <svg class="icon" viewBox="0 0 24 24"><path fill="#e2352f" d="M6.6 10.8a15 15 0 0 0 6.6 6.6l2.2-2.2c.3-.3.7-.4 1-.2 1.1.4 2.3.6 3.6.6.6 0 1 .4 1 1V20c0 .6-.4 1-1 1A17 17 0 0 1 3 4c0-.6.4-1 1-1h3.5c.6 0 1 .4 1 1 0 1.3.2 2.5.6 3.6.1.3 0 .7-.2 1z"/></svg>
      02 5550 1840
    </li>
    <li>
      <svg class="icon" viewBox="0 0 24 24"><path fill="#e2352f" d="M6 3h12v5H6zM4 9h16a2 2 0 0 1 2 2v6h-4v4H6v-4H2v-6a2 2 0 0 1 2-2zm4 7v3h8v-3z"/></svg>
      02 5550 1841
    </li>
    <li>
      <svg class="icon" viewBox="0 0 24 24"><path fill="#e2352f" d="M2 5h20v14H2zm2 2v.5l8 5 8-5V7zm0 3v7h16v-7l-8 5z"/></svg>
      info@brightpaththerapies.example
    </li>
  </ul>

  <div class="staff">
    <p class="staff-name">Clara Whitfield</p>
    <p class="staff-role">Manager</p>
  </div>

  <svg class="band" viewBox="0 0 700 110" preserveAspectRatio="none">
    <path fill="#2a72c0" d="M0 30 Q360 95 700 62 L700 110 L0 110 Z"/>
    <path fill="#e2352f" d="M150 28 Q430 75 700 42 L700 60 Q420 88 150 28 Z"/>
  </svg>
  <p class="web">www.brightpaththerapies.example</p>
</section>

</body>
</html>
```